Veltracore Needs a Poster to Advertise a New Membership Offer

We need a Poster design for Veltracore Fitness Studio.
A first of it's kind membership, The Veltracore Fitness Studio combines the skills of our industry-leading Physiotherapists, Strength Coaches and Massage Therapists into one membership with a tailored plan to guide you through the fundamentals of Movement, Mobility and Recovery.
The concept is loosely based on the professional sports model, where every member of our team works together to produce lasting results for you. The final design should illustrate the bespoke nature of our program in a fun, supportive and professional space.
"Whether your aim is to be the best in the world, or the best in your world – it’s all the same to us."
Brand Guidelines
The poster should be on a black background and use our brand colour, lime green (hexcode #cefa08) as a highlight. Please don't overuse the highlight colour though. Generally, we opt for less bright colours and more of a 'street' look
Target Market(s)
The poster should attract predominantly female members, but should not exclude males. The target age range is 30-40 years female.
Industry/Entity Type
Health And Wellness
Font styles to use
Requirements
Must have
- Must Include
• VFS logo
• Tag line " Building Strong, Mobile, Bulletproof Humans"
• Call to action "Join us"
• Sized to 600(W)x900(H)mm
• Text: "A first of it's kind membership, The Veltracore Fitness Studio combines the skills of our industry-leading Physiotherapists, Strength Coaches and Massage Therapists into one membership with a tailored plan to guide you through the fundamentals of Movement, Mobility and Recovery."
Nice to have
- Ideal Inclusions
• Veltracore logo
• Text "Membership Now Open"
• Web address: veltracore.com.au
Should not have
- Don't Use:
• Too much of the highlight colour
• Cartoon imagery
• Images that are too staged or revealing (clothing). Image should fit our target market of everyday active people, not elite athletes or models.

```html
<!DOCTYPE html>
<html lang="en">
<head>
<meta charset="utf-8">
<title>Veltracore Fitness Studio – Membership Poster</title>
<link href="https://fonts.googleapis.com/css2?family=Oswald:wght@300;400;600;700&display=swap" rel="stylesheet">
<style>
  :root {
    --page-bg: #d9d9d6;
    --poster-bg: #161616;
    --poster-bg-edge: #0d0d0d;
    --ink: #f2f2f2;
    --ink-soft: #e4e4e4;
    --lime: #cefa08;
    --dark-ink: #111111;
    --photo-top: #2a2a2a;
    --photo-mid: #7a1a22;
    --photo-low: #1c1c1c;
  }
  * { box-sizing: border-box; margin: 0; padding: 0; }
  html, body {
    width: 1200px;
    height: 960px;
    overflow: hidden;
    background: var(--page-bg);
    font-family: "Oswald", "Arial Narrow", sans-serif;
  }
  .poster {
    position: absolute;
    left: 300px;
    top: 30px;
    width: 600px;
    height: 900px;
    background: radial-gradient(ellipse at 75% 45%, #1e1e1e 0%, var(--poster-bg) 55%, var(--poster-bg-edge) 100%);
    overflow: hidden;
    color: var(--ink);
  }
  .runner-photo {
    position: absolute;
    left: 392px;
    top: 150px;
    width: 198px;
    height: 700px;
    border-radius: 100px 100px 40px 40px;
    background: linear-gradient(180deg, var(--photo-top) 0%, var(--photo-mid) 22%, var(--photo-mid) 42%, var(--photo-low) 66%, var(--poster-bg) 100%);
    opacity: 0.85;
    z-index: 0;
  }
  .brand, .headline, .cta, .intro, .membership, .web { z-index: 1; }
  .brand {
    position: absolute;
    left: 48px;
    top: 40px;
  }
  .brand-name {
    font-weight: 700;
    font-size: 64px;
    line-height: 1;
    letter-spacing: 1px;
    color: var(--ink);
  }
  .headline {
    position: absolute;
    left: 48px;
    top: 162px;
    font-weight: 600;
    font-size: 44px;
    line-height: 50px;
    text-transform: uppercase;
    color: var(--ink);
  }
  .headline span { display: block; white-space: nowrap; }
  .cta {
    position: absolute;
    left: 48px;
    top: 394px;
    width: 202px;
    height: 74px;
    background: var(--lime);
    border-radius: 4px;
    color: var(--dark-ink);
    font-weight: 700;
    font-size: 46px;
    line-height: 74px;
    text-align: center;
    text-transform: uppercase;
  }
  .intro {
    position: absolute;
    left: 48px;
    top: 500px;
    width: 300px;
    font-weight: 300;
    font-size: 18px;
    line-height: 26px;
    color: var(--ink-soft);
  }
  .membership {
    position: absolute;
    left: 48px;
    top: 730px;
    width: 342px;
    border-top: 2px solid var(--lime);
    border-bottom: 2px solid var(--lime);
    padding: 6px 0 4px;
    font-weight: 600;
    font-size: 33px;
    line-height: 44px;
    text-transform: uppercase;
    white-space: nowrap;
  }
  .membership .accent { color: var(--lime); }
  .web {
    position: absolute;
    left: 48px;
    top: 812px;
    font-weight: 600;
    font-size: 28px;
    line-height: 36px;
    color: var(--ink);
  }
  .web .accent { color: var(--lime); }
</style>
</head>
<body>
  <main class="poster">
    <div class="runner-photo" role="img" aria-label="Photo of a woman jogging toward the viewer in a red sweatshirt, black leggings and white headphones"></div>

    <div class="brand">
      <span class="brand-name">VFS</span>
    </div>

    <h1 class="headline">
      <span>Building Strong,</span>
      <span>Mobile,</span>
      <span>Bulletproof</span>
      <span>Humans</span>
    </h1>

    <div class="cta">Join Us</div>

    <p class="intro">A first of it's kind membership, The Veltracore Fitness Studio combines the skills of our industry-leading Physiotherapists, Strength Coaches and Massage Therapists into one membership with a tailored plan to guide you through the fundamentals of Movement, Mobility and Recovery.</p>

    <div class="membership">Membership <span class="accent">Now Open</span></div>

    <div class="web"><span class="accent">veltracore</span>.com.au</div>
  </main>
</body>
</html>
```